Design an Elegant Handbag Brand website

I need a webiste design are looking for ideas for a new theme, color scheme, etc. You come up with the general look and feel of the home page and our team will take it from there.
We're only looking for a one (1) page layout which should be fashionable and graphic intensive, but also include the standard homepage links (about us, see our collections, etc)

Target Market(s)

Our customers are fashionable women looking for an animal friendly and environmentally friendly handbag.

Industry/Entity Type

Business

Number of Pages Required

1 page

Font styles to use
Serif
Sans Serif

Requirements
Must have
• Feel free to modify it with different colors or tweaks as you see fit. We are open to all suggestions.
Nice to have

```html
<!DOCTYPE html>
<html lang="en">
<head>
<meta charset="utf-8">
<title>Hollis Carry — Handbags</title>
<link href="https://fonts.googleapis.com/css2?family=Montserrat:wght@400;500;600;700&display=swap" rel="stylesheet">
<style>
:root{
  --pink:#e83a72;
  --pink-soft:#f5a3bf;
  --ink:#3b3845;
  --muted:#8a8792;
  --line:#d8b7c4;
  --plum:#5a2a55;
  --plum-deep:#3d1c3d;
  --white:#ffffff;
}
*{margin:0;padding:0;box-sizing:border-box}
html,body{width:1200px;height:4295px;overflow:hidden}
body{position:relative;font-family:'Montserrat',sans-serif;color:var(--ink);background:var(--white)}
.abs{position:absolute}
.glow{position:absolute;border-radius:50%;background:radial-gradient(circle,rgba(246,170,196,.55),rgba(246,170,196,0) 70%)}

/* hero */
.hero{left:0;top:0;width:1200px;height:645px;background:linear-gradient(100deg,#b79a76 0%,#9e7d67 30%,#7a4a6a 60%,#c24d86 85%,#e067a0 100%)}
.hero-shade{left:0;top:0;width:1200px;height:645px;background:linear-gradient(180deg,rgba(60,30,70,.35),rgba(0,0,0,0) 40%)}
.hero-wave{left:0;top:540px;width:1200px;height:110px}
.nav{top:14px;left:200px;width:810px;display:flex;align-items:center;justify-content:space-between}
.brand{display:flex;align-items:center;gap:8px;color:var(--pink);font-weight:600;font-size:24px}
.brand i{width:22px;height:22px;background:var(--pink);border-radius:4px;display:block}
.menu{display:flex;gap:22px;font-size:11px;color:var(--white)}
.menu .on{color:var(--pink);border-bottom:1px solid var(--pink);padding-bottom:2px}
.hero-box{left:222px;top:160px;width:345px;height:228px;border:3px solid var(--pink);border-top-color:transparent;text-align:center;color:var(--white)}
.hero-box:before{content:"";position:absolute;left:-3px;top:-3px;width:150px;height:3px;background:var(--pink)}
.hero-box h1{font-weight:600;font-size:34px;letter-spacing:3px;line-height:1.2;margin-top:26px}
.hero-box h1 b{color:var(--pink);font-weight:600}
.hero-box h1 .big{font-size:40px}
.hero-box p{font-size:13px;line-height:1.6;margin-top:8px}
.btn{display:inline-block;background:var(--pink);color:var(--white);border-radius:20px;font-size:14px;text-align:center;box-shadow:0 6px 14px rgba(232,58,114,.35)}
.dots{display:flex;gap:14px;align-items:center}
.dots span{width:12px;height:12px;border-radius:50%;background:#f1e7ee}
.dots .cur{width:18px;height:18px;border:3px solid var(--pink);background:#fff;box-shadow:inset 0 0 0 3px #fff,inset 0 0 0 9px var(--pink)}
.side-icons{right:0;top:190px;display:flex;flex-direction:column;gap:18px}
.side-icons span{width:38px;height:38px;background:#f08a4b;border-radius:6px 0 0 6px;display:flex;align-items:center;justify-content:center}

/* section heading */
.sec{left:0;width:1200px;text-align:center}
.sec .rule{width:95px;height:1px;background:var(--line);margin:0 auto}
.sec h2{font-weight:500;font-size:38px;margin:12px 0 10px}
.sec h2 b{color:var(--pink);font-weight:500}
.sec .mark{display:flex;align-items:center;justify-content:center;gap:10px}
.sec .mark:before,.sec .mark:after{content:"";width:75px;height:1px;background:var(--line)}
.sec .mark i{width:12px;height:10px;background:var(--pink);border-radius:2px 2px 3px 3px;display:block}
.sec.light h2{color:var(--white)}
.sec.light .rule,.sec.light .mark:before,.sec.light .mark:after{background:rgba(255,255,255,.5)}
.sec.light .mark i{background:#fff}

/* collections */
.card{top:850px;width:180px;height:218px;background:#fff;text-align:center;font-size:12px;box-shadow:0 2px 10px rgba(0,0,0,.06)}
.card.lift{box-shadow:0 8px 24px rgba(0,0,0,.14)}
.card .ph{margin:22px auto 0;width:120px;height:100px;border-radius:10px}
.card .heart{position:absolute;right:10px;top:8px}
.card h3{font-weight:400;font-size:12px;margin-top:22px}
.card .price{margin-top:10px}
.card .price b{color:var(--pink);font-weight:400}
.card .more{margin-top:10px;font-size:11px}
.card.lift .more{color:var(--pink)}

/* about */
.about-frame{left:197px;top:1377px;width:356px;height:403px;border:1.5px solid #c9678f;border-radius:0 40px 0 40px}
.about-photo{left:222px;top:1398px;width:360px;height:362px;border-radius:0 50px 0 40px;background:linear-gradient(135deg,#cdbb8a,#a67b52 45%,#c27b82 80%,#d59bb4)}
.about-text{left:618px;top:1392px;width:385px}
.about-text h3{font-weight:500;font-size:19px;line-height:1.6}
.about-text p{font-size:11.5px;color:var(--muted);line-height:1.64;margin-top:26px}

/* process */
.process{left:0;top:1862px;width:1200px;height:401px;background:linear-gradient(100deg,#6e5e3c 0%,#7a5a44 35%,#7a3c5a 70%,#8a3b6a 100%)}
.step{top:2050px;width:220px;text-align:center;color:#fff}
.step h4{font-weight:600;font-size:16px;margin-top:12px}
.step p{font-size:11px;line-height:1.5;margin-top:6px;color:rgba(255,255,255,.85)}

/* blog */
.post{left:193px;width:382px;background:#f7f3f5;display:flex;font-size:11.5px}
.post .date{width:50px;background:var(--pink);color:#fff;font-size:10px;padding:12px 0 0 14px;line-height:1.3}
.post .txt{padding:12px 8px;line-height:1.5}
.post.main{height:155px;background:#fff;box-shadow:0 4px 16px rgba(0,0,0,.08);display:block}
.post.main .head{display:flex;background:#fbf0f4}
.post.main .head .txt{color:var(--pink)}
.post.main .body{padding:10px 14px;font-size:10px;color:var(--muted);line-height:1.65}
.post.main .foot{display:flex;justify-content:space-between;padding:0 14px;font-size:9.5px;color:var(--pink)}
.blog-frame{left:618px;top:2477px;width:360px;height:398px;border:1.5px solid #c9678f;border-radius:30px 0 30px 0}
.blog-photo{left:642px;top:2497px;width:361px;height:360px;border-radius:0 40px 0 0;background:linear-gradient(160deg,#e9d3a8,#cc8a45 45%,#d58ea0 90%)}

/* promo */
.promo{left:195px;top:3018px;width:810px;height:207px;background:linear-gradient(100deg,#e7ecf7 0%,#fff 45%,#fff 100%);box-shadow:0 4px 18px rgba(0,0,0,.1);border-radius:6px}
.promo h3{position:absolute;left:48px;top:42px;color:var(--pink);font-weight:700;font-size:34px;letter-spacing:2px}
.promo h4{position:absolute;left:48px;top:92px;font-weight:600;font-size:22px;letter-spacing:1px;color:#f08a4b}
.promo h4 b{color:#3b3e66}
.promo-bags{left:640px;top:3030px;width:360px;height:190px;border-radius:8px;background:linear-gradient(90deg,#2a2a2e 0 25%,#fff 25% 32%,#c8a582 32%,#dcc0a2)}

/* testimonials */
.avatar{left:570px;top:3417px;width:60px;height:60px;border-radius:50%;background:linear-gradient(135deg,#f1c7bd,#c26a56);border:3px solid #f4dbe4}
.quote{font-size:150px;color:#f7dce6;font-family:Georgia,serif;line-height:1}
.arrow-btn{width:26px;height:26px;border-radius:50%;background:#fff;box-shadow:0 2px 8px rgba(0,0,0,.18);display:flex;align-items:center;justify-content:center}

/* contact */
.contact{left:0;top:3700px;width:1200px;height:595px}
.foot-col{top:3905px;color:#fff}
.foot-col h4{font-weight:600;font-size:18px;margin-bottom:24px}
.foot-col li{list-style:none;font-size:11px;line-height:25px}
.info li{display:flex;gap:10px;margin-bottom:10px;line-height:1.7}
.field{border-bottom:1px solid rgba(255,255,255,.5);font-size:10px;height:36px;padding-top:12px;color:#fff}
.social{display:flex;gap:36px}
.social span{width:20px;height:20px;border:2px solid #fff;border-radius:50%}
</style>
</head>
<body>

<!-- HERO -->
<div class="abs hero" role="img" aria-label="Photo of a smiling woman holding shopping bags in front of a handbag shop window"></div>
<div class="abs hero-shade"></div>
<svg class="abs hero-wave" viewBox="0 0 1200 110" preserveAspectRatio="none"><path d="M0 30 Q600 180 1200 30 L1200 110 L0 110 Z" fill="#fff"/></svg>

<nav class="abs nav">
  <div class="brand"><i></i>Hollis Carry</div>
  <div class="menu"><span class="on">Home</span><span>Our Collections</span><span>About Us</span><span>Blog</span><span>Testimonial</span><span>Contact Us</span></div>
</nav>

<div class="abs hero-box">
  <h1>FALL IN <b>LOVE</b><br>WITH YOUR<br><span class="big"><b>BAG</b> AGAIN</span></h1>
  <p>Lorem ipsum dolor sit amet,<br>consetetur sadipscing elitr, sed diam</p>
</div>
<a class="abs btn" style="left:332px;top:422px;width:125px;height:35px;line-height:35px">Shop Now</a>
<div class="abs dots" style="left:540px;top:549px"><span></span><span></span><span class="cur"></span><span></span><span></span></div>

<div class="abs side-icons">
  <span><svg width="16" height="16" viewBox="0 0 24 24" fill="none" stroke="#fff" stroke-width="2"><path d="M12 21l-8-8a5 5 0 017-7l1 1 1-1a5 5 0 017 7z"/></svg></span>
  <span><svg width="16" height="16" viewBox="0 0 24 24" fill="none" stroke="#fff" stroke-width="2"><path d="M2 3h3l3 12h11l2-8H6"/><circle cx="9" cy="20" r="1.5"/><circle cx="18" cy="20" r="1.5"/></svg></span>
  <span><svg width="16" height="16" viewBox="0 0 24 24" fill="none" stroke="#fff" stroke-width="2"><circle cx="12" cy="8" r="4"/><path d="M4 21c0-4 4-6 8-6s8 2 8 6"/></svg></span>
  <span><svg width="16" height="16" viewBox="0 0 24 24" fill="none" stroke="#fff" stroke-width="2"><circle cx="10" cy="10" r="6"/><path d="M15 15l6 6"/></svg></span>
</div>

<div class="glow" style="left:980px;top:1000px;width:300px;height:300px"></div>
<div class="glow" style="left:-120px;top:1700px;width:260px;height:260px"></div>
<div class="glow" style="left:1000px;top:3300px;width:280px;height:280px"></div>

<!-- COLLECTIONS -->
<div class="abs sec" style="top:705px"><div class="rule"></div><h2>Our <b>Collections</b></h2><div class="mark"><i></i></div></div>

<div class="abs card" style="left:205px">
  <svg class="heart" width="14" height="14" viewBox="0 0 24 24" fill="none" stroke="#999" stroke-width="2"><path d="M12 21l-8-8a5 5 0 017-7l1 1 1-1a5 5 0 017 7z"/></svg>
  <div class="ph" role="img" aria-label="Grey and tan leather satchel" style="background:linear-gradient(90deg,#a97a66,#9a9a9c 50%,#c87a78)"></div>
  <h3>Bag Company Name</h3><div class="price">Price : <b>$120</b></div><div class="more">View Details ⟶</div>
</div>
<div class="abs card lift" style="left:407px">
  <svg class="heart" width="14" height="14" viewBox="0 0 24 24" fill="#e83a72"><path d="M12 21l-8-8a5 5 0 017-7l1 1 1-1a5 5 0 017 7z"/></svg>
  <div class="ph" role="img" aria-label="Red leather handbag" style="background:linear-gradient(160deg,#e23a3a,#a31318)"></div>
  <h3>Bag Company Name</h3><div class="price">Price : <b>$120</b></div><div class="more">View Details ⟶</div>
</div>
<div class="abs card" style="left:610px">
  <svg class="heart" width="14" height="14" viewBox="0 0 24 24" fill="none" stroke="#999" stroke-width="2"><path d="M12 21l-8-8a5 5 0 017-7l1 1 1-1a5 5 0 017 7z"/></svg>
  <div class="ph" role="img" aria-label="Navy leather handbag" style="background:linear-gradient(160deg,#4a4f6c,#1f2233)"></div>
  <h3>Bag Company Name</h3><div class="price">Price : <b>$120</b></div><div class="more">View Details ⟶</div>
</div>
<div class="abs card" style="left:812px">
  <svg class="heart" width="14" height="14" viewBox="0 0 24 24" fill="none" stroke="#999" stroke-width="2"><path d="M12 21l-8-8a5 5 0 017-7l1 1 1-1a5 5 0 017 7z"/></svg>
  <div class="ph" role="img" aria-label="Rust brown leather handbag" style="background:linear-gradient(160deg,#c46a55,#8d3f32)"></div>
  <h3>Bag Company Name</h3><div class="price">Price : <b>$120</b></div><div class="more">View Details ⟶</div>
</div>
<a class="abs btn" style="left:537px;top:1120px;width:125px;height:35px;line-height:35px">Shop Now</a>

<!-- ABOUT -->
<div class="abs sec" style="top:1225px"><div class="rule"></div><h2>About <b>Us</b></h2><div class="mark"><i></i></div></div>
<div class="abs about-frame"></div>
<div class="abs about-photo" role="img" aria-label="Open tan leather bag with glasses and a lipstick"></div>
<div class="abs about-text">
  <h3>Lorem Ipsum Is Simply Dummy Text Of The Printing And Typesetting Industry</h3>
  <p>Contrary to popular belief, Lorem Ipsum is not simply random text. It has roots in a piece of classical Latin literature from 45 BC, making it over 2000 years old. Edwin Hartley, a Latin professor at Ashcombe College in Virginia, looked up one of the more obscure Latin words, consectetur, from a Lorem Ipsum passage, and going through the cites of the word in classical literature, discovered the undoubtable source. Contrary to popular belief, Lorem Ipsum is not simply random text. It has roots in a piece of classical Latin literature from 45 BC, making it over 2000 years old. Edwin Hartley, a Latin professor at Ashcombe College in Virginia, looked up one of the more obscure Latin words.</p>
</div>
<a class="abs btn" style="left:618px;top:1725px;width:125px;height:35px;line-height:35px">Read More</a>

<!-- PROCESS -->
<div class="abs process" role="img" aria-label="Close-up of a tan leather bag"></div>
<div class="abs sec light" style="top:1902px;left:-15px"><div class="rule"></div><h2>Our Process</h2><div class="mark"><i></i></div></div>

<div class="abs step" style="left:167px">
  <svg width="42" height="38" viewBox="0 0 42 38" fill="none" stroke="#fff" stroke-width="2.5"><rect x="4" y="10" width="30" height="20" rx="2" transform="rotate(-15 19 20)"/><path d="M6 16l28-8"/></svg>
  <h4>Secure Online Payment</h4><p>Lorem ipsum dolor sit amet,<br>consetetur sadipscing elitr,<br>sed diam nonumy eirmod</p>
</div>
<div class="abs step" style="left:383px">
  <svg width="42" height="38" viewBox="0 0 42 38" fill="none" stroke="#fff" stroke-width="2.5"><path d="M8 14l13-7 13 7v16l-13 6-13-6z"/><path d="M8 14l13 7 13-7M21 21v15"/></svg>
  <h4>Discreet Packaging</h4><p>Lorem ipsum dolor sit amet,<br>consetetur sadipscing elitr,<br>sed diam nonumy eirmod</p>
</div>
<div class="abs step" style="left:597px">
  <svg width="50" height="38" viewBox="0 0 50 38" fill="#fff"><rect x="2" y="8" width="28" height="20" rx="2"/><path d="M32 14h9l6 7v7H32z"/><circle cx="12" cy="31" r="4"/><circle cx="39" cy="31" r="4"/></svg>
  <h4>Fast Shipping</h4><p>Lorem ipsum dolor sit amet,<br>consetetur sadipscing elitr,<br>sed diam nonumy eirmod</p>
</div>
<div class="abs step" style="left:812px">
  <svg width="42" height="38" viewBox="0 0 42 38" fill="none" stroke="#fff" stroke-width="2.5"><path d="M5 8h32l3 8H2z"/><path d="M6 16v18h30V16M15 34v-9h12v9"/><path d="M12 2h18"/></svg>
  <h4>Store Pickup Option</h4><p>Lorem ipsum dolor sit amet,<br>consetetur sadipscing elitr,<br>sed diam nonumy eirmod</p>
</div>

<!-- BLOG -->
<div class="abs sec" style="top:2320px"><div class="rule"></div><h2>Our <b>Blog</b></h2><div class="mark"><i></i></div></div>

<div class="abs post main" style="top:2497px">
  <div class="head"><div class="date">7th<br>SEP</div><div class="txt">Here Will be your blog title. Lorem Ipsum has been the industry's standard dummy text ever..</div></div>
  <div class="body">Lorem Ipsum has been the industry's standard dummy text ever since the 1500s, when an unknown printer took a galley of type and scrambled it to make a type specimen book.ever since the 1500s, when an unknown printer took a galley of type and scrambled it to make</div>
  <div class="foot"><span>◦ Ada Renn</span><span>Read More ⟶</span></div>
</div>
<div class="abs post" style="top:2668px;height:50px"><div class="date">15th<br>SEP</div><div class="txt">Lorem Ipsum has been the industry's standard dummy text ever since the 1500s</div></div>
<div class="abs post" style="top:2737px;height:50px"><div class="date">15th<br>SEP</div><div class="txt">Lorem Ipsum has been the industry's standard dummy text ever since the 1500s</div></div>
<div class="abs post" style="top:2806px;height:50px"><div class="date">15th<br>SEP</div><div class="txt">Lorem Ipsum has been the industry's standard dummy text ever since the 1500s</div></div>

<div class="abs blog-frame"></div>
<div class="abs blog-photo" role="img" aria-label="Tan tooled leather duffel handbag"></div>
<a class="abs btn" style="left:530px;top:2925px;width:138px;height:40px;line-height:40px">Learn More</a>

<!-- PROMO -->
<div class="abs promo">
  <h3>UP TO 50% OFF</h3>
  <h4>Use This Code <b>#12345</b></h4>
  <a class="btn" style="position:absolute;left:48px;top:137px;width:108px;height:35px;line-height:35px;font-size:13px">Shop Now</a>
</div>
<div class="abs promo-bags" role="img" aria-label="Black tote bag and a beige handbag set"></div>

<!-- TESTIMONIALS -->
<div class="abs sec" style="top:3292px"><div class="rule" style="width:140px"></div><h2>Our <b>Testimonials</b></h2><div class="mark"><i></i></div></div>
<div class="abs avatar" role="img" aria-label="Customer portrait"></div>
<div class="abs" style="left:0;top:3488px;width:1200px;text-align:center;color:var(--pink);font-size:16px;font-weight:500">Mara Quinlan</div>
<div class="abs quote" style="left:255px;top:3470px">“</div>
<div class="abs quote" style="left:868px;top:3560px">”</div>
<p class="abs" style="left:340px;top:3520px;width:520px;text-align:center;font-size:11px;line-height:1.65;color:var(--muted)">Lorem Ipsum is simply dummy text of the printing and typesetting industry. Lorem Ipsum has been the industry's standard dummy text ever since the 1500s, when an unknown printer took a galley of type and scrambled it to make a type specimen book. It has survived not only five centuries, but also the leap into electronic.</p>
<div class="abs arrow-btn" style="left:209px;top:3524px"><svg width="10" height="10" viewBox="0 0 10 10" fill="none" stroke="#333" stroke-width="1.5"><path d="M6 2L3 5l3 3"/></svg></div>
<div class="abs arrow-btn" style="left:962px;top:3524px"><svg width="10" height="10" viewBox="0 0 10 10" fill="none" stroke="#333" stroke-width="1.5"><path d="M4 2l3 3-3 3"/></svg></div>
<div class="abs dots" style="left:540px;top:3621px"><span style="background:#f7d6e2"></span><span style="background:#f7d6e2"></span><span class="cur"></span><span style="background:#f7d6e2"></span><span style="background:#f7d6e2"></span></div>

<!-- CONTACT -->
<svg class="abs contact" viewBox="0 0 1200 595" preserveAspectRatio="none" role="img" aria-label="Woven rattan bag in warm dim light">
  <defs><linearGradient id="contactBg" x1="0" x2="1"><stop offset="0" stop-color="#5a4a32"/><stop offset=".45" stop-color="#4a2a3a"/><stop offset="1" stop-color="#6a2a4e"/></linearGradient></defs>
  <path d="M0 80 Q600 -60 1200 80 V595 H0 Z" fill="url(#contactBg)"/>
</svg>
<div class="abs sec light" style="top:3780px"><h2 style="margin:0 0 10px">Contact Us</h2><div class="mark"><i></i></div></div>

<div class="abs foot-col" style="left:212px;width:200px">
  <h4>Contact Us</h4>
  <ul class="info">
    <li>◉<span>Lindenweg 14b Lorem<br>52180 Ipsum</span></li>
    <li style="margin-top:26px">▯<span>Mobile +00 (0) 555 018 274</span></li>
    <li>✆<span>Tel : +00 (0) 555 018 274</span></li>
    <li>▣<span>Fax: +00 (0) 555 - 0193 462</span></li>
    <li>◎<span>E-Mail: hello@holliscarry.test</span></li>
  </ul>
</div>
<div class="abs foot-col" style="left:518px;width:180px">
  <h4>Shop Service</h4>
  <ul><li>Affiliate Program</li><li>Contact</li><li>Shipping</li><li>Payment Terms</li><li>Return</li><li>Withdrawal</li><li>Terms of Service</li></ul>
</div>
<div class="abs foot-col" style="left:780px;width:215px">
  <h4 style="padding-left:52px">Contact Us</h4>
  <div class="field" style="margin-top:-12px">Name</div>
  <div class="field">Email Address</div>
  <div class="field">Phone Number</div>
  <div class="field" style="height:68px;padding-top:44px">Your Message</div>
  <a class="btn" style="display:block;margin:22px 0 0 60px;width:88px;height:30px;line-height:30px;font-size:13px">Submit</a>
</div>
<div class="abs social" style="left:512px;top:4192px" aria-label="Social links"><span></span><span></span><span></span><span></span></div>
<div class="abs" style="left:0;top:4265px;width:1200px;height:1px;background:rgba(255,255,255,.3)"></div>
<div class="abs" style="left:0;top:4275px;width:1200px;text-align:center;font-size:10px;color:#fff">Copyright © 2020 By <span style="color:var(--pink)">Company Name</span>. All rights reserved</div>

</body>
</html>
```